PIPE RELINING COMPANY NEEDS A NEW INFORMATIVE FLYER CREATED

We are a company that sells a service to residential homeowners (using a particular state of the art international product) and we need to refresh our A4 tri- fold flyer (z fold 6 pages). The layout needs to include pictures, heading and text boxes, but be simple and clean cut at the same time.

The front of the flyer must have the attached picture of the pipe under the house, logo and website.

This flyer is going to be given to clients and to leave with them when we quote for work.

Our colour scheme is black, white, red. A highlight colour if needed (in small amounts) could be 100% cyan and also a bright orange.

I have attached the copy of the text and this can be spread out throughout the brochure.

We are a professional and industry leading company so it needs to be professional, clean cut but with a modern edge.

Target Market(s)

HOMEOWNERS

Industry/Entity Type

It Company

Font styles to use
Sans Serif

Colors
ec1f27
ffffff
000000
f37122

Requirements
Must have
• PROFESSINAL, MODERN
• USE OF BLACK, RED AND WHITE - REFER LOGO
Should not have
• BE CLUTTERED

```html
<!DOCTYPE html>
<html lang="en">
<head>
<meta charset="utf-8">
<title>ClearBore Pipe Relining – Tri-fold Flyer</title>
<link href="https://fonts.googleapis.com/css2?family=Open+Sans:ital,wght@0,400;0,600;0,700;0,800;1,400&family=Kaushan+Script&display=swap" rel="stylesheet">
<style>
  :root {
    --red: #ec1f27;
    --black: #111111;
    --panel-dark: #1b1b1b;
    --white: #ffffff;
    --grey: #d9d9d9;
    --text-dark: #222222;
    --photo-sky: #9fb8c9;
    --photo-grass: #5c7a35;
    --photo-soil: #6b4a32;
  }
  * { box-sizing: border-box; margin: 0; padding: 0; }
  html, body {
    width: 1200px; height: 800px; overflow: hidden;
    background: #e6e6e6;
    font-family: "Open Sans", Arial, sans-serif;
  }
  .flyer { position: relative; width: 1200px; height: 800px; overflow: hidden; }
  .flyer-art { position: absolute; inset: 0; }
  .abs { position: absolute; }

  /* Left panel */
  .info-photo {
    left: 40px; top: 70px; width: 190px; height: 190px; border-radius: 50%;
    border: 6px solid var(--black);
    background: radial-gradient(circle at 40% 40%, #8a8f96, #2a2c30);
  }
  .info-heading {
    left: 36px; top: 282px; width: 330px;
    font-size: 15px; font-weight: 700; color: var(--black); text-align: center;
    text-transform: uppercase; letter-spacing: .3px;
  }
  .info-list { left: 36px; top: 312px; width: 330px; list-style: none; }
  .info-list li { font-size: 11.2px; line-height: 1.32; color: var(--text-dark); margin-bottom: 6px; text-align: justify; }
  .info-list strong { color: var(--red); font-weight: 700; }
  .seal {
    left: 262px; top: 540px; display: flex; align-items: center; gap: 8px;
  }
  .seal-dot { width: 22px; height: 22px; border-radius: 50%; background: var(--red); }
  .seal-name { font-size: 18px; font-weight: 800; color: var(--black); }
  .contact-line {
    left: 30px; top: 700px; width: 340px; text-align: center;
    color: var(--white); font-size: 14.5px; line-height: 1.45;
  }

  /* Middle panel */
  .benefits { left: 440px; top: 40px; width: 330px; list-style: none; }
  .benefits li {
    position: relative; padding-left: 24px; margin-bottom: 12px;
    color: var(--white); font-size: 11.5px; line-height: 1.35; text-transform: uppercase;
  }
  .benefits svg { position: absolute; left: 0; top: 1px; }
  .call { left: 440px; top: 640px; width: 330px; }
  .call-label { color: var(--red); font-size: 14px; font-weight: 600; text-transform: uppercase; margin-left: 44px; }
  .call-number { display: flex; align-items: center; gap: 10px; color: var(--white); font-size: 38px; font-weight: 700; letter-spacing: 1px; }

  /* Right panel */
  .brand-name {
    left: 830px; top: 40px; width: 340px; text-align: center;
    color: var(--white); font-size: 38px; font-weight: 800; letter-spacing: -.5px;
  }
  .tagline { left: 830px; top: 605px; width: 340px; text-align: center; color: var(--white); font-size: 15px; line-height: 1.45; }
  .script { left: 830px; top: 656px; width: 340px; text-align: center; color: var(--red); font-family: "Kaushan Script", cursive; font-size: 22px; }
  .web-button {
    left: 880px; top: 706px; width: 240px; height: 36px; border-radius: 18px;
    background: var(--red); color: var(--white);
    display: flex; align-items: center; justify-content: center;
    font-size: 15px; font-weight: 600;
  }
</style>
</head>
<body>
<main class="flyer">
  <svg class="flyer-art" width="1200" height="800" viewBox="0 0 1200 800" aria-hidden="true">
    <defs>
      <linearGradient id="sceneGrad" x1="0" y1="0" x2="0" y2="1">
        <stop offset="0" stop-color="#9fb8c9"/>
        <stop offset=".45" stop-color="#8c8a70"/>
        <stop offset=".65" stop-color="#5c7a35"/>
        <stop offset="1" stop-color="#6b4a32"/>
      </linearGradient>
      <radialGradient id="insetGrad" cx=".5" cy=".5" r=".6">
        <stop offset="0" stop-color="#b08a62"/>
        <stop offset="1" stop-color="#5d4a36"/>
      </radialGradient>
    </defs>
    <!-- left panel -->
    <rect x="0" y="0" width="400" height="800" fill="#ffffff"/>
    <path d="M0 0 H400 V30 C300 60 220 40 160 90 C120 130 60 180 0 190 Z" fill="#ec1f27"/>
    <path d="M160 90 C220 40 300 60 400 30 V170 C330 110 250 100 160 90 Z" fill="#ec1f27"/>
    <path d="M0 600 C120 640 260 650 400 560 V620 C260 700 120 700 0 680 Z" fill="#ec1f27"/>
    <path d="M0 680 C120 700 260 700 400 620 V800 H0 Z" fill="#151515"/>
    <!-- middle + right panels -->
    <rect x="400" y="0" width="800" height="800" fill="#1b1b1b"/>
    <path d="M400 250 C520 240 650 200 800 200 C900 200 1000 150 1200 150 V600 C1050 600 900 560 800 600 C650 650 520 600 400 620 Z" fill="url(#sceneGrad)"/>
    <path d="M400 250 C520 240 650 200 800 200 C900 200 1000 150 1200 150" fill="none" stroke="#ffffff" stroke-width="5"/>
    <path d="M400 620 C520 600 650 650 800 600 C900 560 1050 600 1200 600" fill="none" stroke="#ec1f27" stroke-width="3"/>
    <line x1="400" y1="0" x2="400" y2="800" stroke="#000" stroke-opacity=".25"/>
    <line x1="800" y1="0" x2="800" y2="800" stroke="#000" stroke-opacity=".25"/>
  </svg>

  <div class="abs" role="img" aria-label="Photo of a tree root system wrapped around a broken clay drain beneath a suburban lawn and house" style="left:400px;top:200px;width:800px;height:420px;"></div>
  <div class="abs" role="img" aria-label="Close-up photo of a new green liner pipe inside an old cracked clay pipe" style="left:700px;top:190px;width:170px;height:170px;border-radius:50%;border:5px solid #ffffff;background:radial-gradient(circle at 50% 50%, #b08a62, #5d4a36);"></div>

  <!-- Left panel -->
  <div class="abs info-photo" role="img" aria-label="Photo of a technician crouching beside the relining service truck"></div>
  <h2 class="abs info-heading">Things you should know</h2>
  <ul class="abs info-list">
    <li><strong>Knowledge &amp; Experience</strong> - We train other plumbers and have been doing it for over 10 years.</li>
    <li><strong>We're An Owned &amp; Operated Business</strong> - We take great pride in our work. Our business is based on relationships not transactions.</li>
    <li><strong>We Use the best in class pipe relining solution</strong> - We have sourced the best products and equipment from around the world and our FlexLine product is from Germany.</li>
    <li><strong>We have state of the art equipment</strong> - Our truck is custom designed and fully equipped with latest technology to carry out pipe relining.</li>
    <li><strong>We're Fully licensed &amp; Insured</strong> - All of our technicians are fully licensed and qualified to complete the job. Our company is fully insured and are happy to provide you with documentation.</li>
    <li><strong>After Sales Service</strong> - We don't forget about you after the job and as part of the warranty we carry out an annual camera inspection of the drainage.</li>
  </ul>
  <div class="abs seal"><span class="seal-dot"></span><span class="seal-name">ClearBore</span></div>
  <p class="abs contact-line">Contact “ClearBore” Pipe Relining<br>Sydney Wide For Best Rates 7 Days</p>

  <!-- Middle panel -->
  <ul class="abs benefits">
    <li><svg width="14" height="14" viewBox="0 0 14 14"><circle cx="7" cy="7" r="6" fill="none" stroke="#ec1f27" stroke-width="1.5"/><path d="M4 7 L6.2 9.2 L10 4.8" fill="none" stroke="#ec1f27" stroke-width="1.6"/></svg>ClearBore uses epoxy resin not polyester or silicate resins.</li>
    <li><svg width="14" height="14" viewBox="0 0 14 14"><circle cx="7" cy="7" r="6" fill="none" stroke="#ec1f27" stroke-width="1.5"/><path d="M4 7 L6.2 9.2 L10 4.8" fill="none" stroke="#ec1f27" stroke-width="1.6"/></svg>ClearBore inverts the liner instead of using a drag-in method.</li>
    <li><svg width="14" height="14" viewBox="0 0 14 14"><circle cx="7" cy="7" r="6" fill="none" stroke="#ec1f27" stroke-width="1.5"/><path d="M4 7 L6.2 9.2 L10 4.8" fill="none" stroke="#ec1f27" stroke-width="1.6"/></svg>ClearBore uses a German system called Linatec.</li>
    <li><svg width="14" height="14" viewBox="0 0 14 14"><circle cx="7" cy="7" r="6" fill="none" stroke="#ec1f27" stroke-width="1.5"/><path d="M4 7 L6.2 9.2 L10 4.8" fill="none" stroke="#ec1f27" stroke-width="1.6"/></svg>ClearBore provides a 25 year warranty</li>
  </ul>
  <div class="abs call">
    <p class="call-label">Call for your quote today</p>
    <p class="call-number">
      <svg width="32" height="32" viewBox="0 0 32 32" aria-hidden="true"><circle cx="16" cy="16" r="14" fill="none" stroke="#fff" stroke-width="2.5"/><path d="M11 9 C10 12 12 18 16 21 C19 23 21 23 23 22 L21 19 L18.5 20 C16.5 19 13.5 16 13 13.5 L14 11 Z" fill="#fff"/></svg>
      02 9000 4821
    </p>
  </div>

  <!-- Right panel -->
  <h1 class="abs brand-name">ClearBore</h1>
  <p class="abs tagline">A fast, clean, permanent solution<br>for fixing blocked drains.</p>
  <p class="abs script">A new pipe within the old</p>
  <p class="abs web-button">www.clearbore.com.au</p>
</main>
</body>
</html>
```